"Got Radon?" Banner Ads

I need banner ads made for Pelvaro Banner Circuit campaign. There are 10 sizes of banners, so I need all 10 sizes. All of them can be similar in design and concept, but need to look good and the content must fill the space nicely.

The text on the ad is "Got Radon?" big/bold, and there should be a picture of a house with gas seeping into it from the ground. I have attached an example of an existing ad for reference.

These are the 10 sizes of banners that we need:
970x90
120x600
160x600
200x200
250x250
350x250
300x600
336x280
468x60
728x90

```html
<!DOCTYPE html>
<html lang="en">
<head>
<meta charset="utf-8">
<title>Got Radon? Banner 336x280</title>
<link rel="stylesheet" href="https://fonts.googleapis.com/css2?family=Anton&family=Montserrat:wght@700&family=Roboto+Condensed:ital,wght@1,700&display=swap">
<style>
  :root {
    --stage: #f2f2f2;
    --stage-edge: #d9d9d9;
    --ink-black: #000000;
    --radon-green: #2bff2b;
    --radon-green-bright: #39ff4a;
    --radon-green-deep: #0b5e0b;
    --text-white: #ffffff;
    --roof-orange: #d8662c;
    --wall-cream: #efe2c8;
    --lawn-green: #4ea82a;
  }
  * { margin: 0; padding: 0; box-sizing: border-box; }
  html, body {
    width: 1200px;
    height: 801px;
    overflow: hidden;
  }
  body {
    background: radial-gradient(ellipse at center, var(--stage) 45%, var(--stage-edge) 100%);
    position: relative;
  }
  .banner {
    position: absolute;
    left: 334px;
    top: 179px;
    width: 532px;
    height: 443px;
    overflow: hidden;
    background: linear-gradient(180deg, var(--ink-black) 0%, var(--ink-black) 40%, #0a4a0a 62%, #18b818 82%, var(--radon-green-bright) 100%);
  }
  .brand {
    position: absolute;
    left: 28px;
    top: 20px;
    color: var(--radon-green);
    font-family: "Montserrat", Arial, sans-serif;
    font-weight: 700;
    font-variant: small-caps;
    font-size: 31px;
    letter-spacing: 2px;
    line-height: 1;
  }
  .tagline {
    position: absolute;
    left: 30px;
    top: 56px;
    color: var(--text-white);
    font-family: "Montserrat", Arial, sans-serif;
    font-weight: 700;
    font-variant: small-caps;
    font-size: 15px;
    letter-spacing: 2px;
    line-height: 1;
  }
  .house-art {
    position: absolute;
    left: 206px;
    top: 84px;
    width: 276px;
    height: 226px;
    border-radius: 10px;
    background: linear-gradient(180deg, var(--roof-orange) 0%, var(--wall-cream) 48%, var(--lawn-green) 78%, var(--radon-green) 100%);
  }
  .offers {
    position: absolute;
    left: 28px;
    top: 194px;
    list-style: none;
    color: var(--text-white);
    font-family: "Roboto Condensed", Arial, sans-serif;
    font-style: italic;
    font-weight: 700;
    font-size: 21px;
    line-height: 27px;
  }
  .headline {
    position: absolute;
    left: 0;
    right: 0;
    top: 322px;
    text-align: center;
    font-family: "Anton", Impact, sans-serif;
    font-size: 98px;
    line-height: 1;
    color: var(--radon-green-bright);
    -webkit-text-stroke: 3px var(--radon-green-deep);
    letter-spacing: 1px;
  }
</style>
</head>
<body>
  <section class="banner">
    <h1 class="brand">Clearstead Radon</h1>
    <p class="tagline">Quality Mitigation Systems</p>
    <div class="house-art" role="img" aria-label="Illustration of a house with green radon gas seeping up from the ground"></div>
    <ul class="offers">
      <li>FREE Estimates</li>
      <li>Same Day Service</li>
      <li>Best Price Guarantee</li>
    </ul>
    <p class="headline">GOT RADON?</p>
  </section>
</body>
</html>
```